Rig up a website for a Rigging Company

We already have a logo. Looking for a website design that works on plivano.com.
Our rigging company uses semi trucks, forklifts, and similar equipment to move large machines.
Our logo is white, black and red.

Target Market(s)

Medical Industry (moving medical equipment), Utility Industry (power equipment), Food Industry (moving bottling/packing equipment), US Government (large equipment)

Industry/Entity Type

It Company

Coding

Coded - Design and coding required

Number of Pages Required

5+ page

Font styles to use
Sans Serif

Colors
ec1f27
ffffff
0355a3

Requirements
Must have
• Home page, About page, Services Page, and Contact Information page
Nice to have
• Pictures of semi and forklifts and ability to insert our own pictures of our equipment

```html
<!DOCTYPE html>
<html lang="en">
<head>
<meta charset="utf-8">
<title>Marlow Rigging</title>
<link rel="stylesheet" href="https://fonts.googleapis.com/css2?family=Montserrat:wght@700;800&family=Open+Sans:wght@400;600&family=Raleway:wght@500;600;700;800&display=swap">
<style>
:root{
  --red:#ec1f27;
  --ink:#111111;
  --text:#333333;
  --muted:#555555;
  --white:#ffffff;
  --footer:#0e0e0e;
  --footer-deep:#060606;
  --footer-text:#b9b9b9;
  --rule:#e6e6e6;
  --partner:#c4c4c4;
}
*{box-sizing:border-box;margin:0;padding:0}
html,body{width:1200px;height:2590px;overflow:hidden;background:var(--white)}
body{font-family:"Open Sans",Arial,sans-serif;color:var(--text);position:relative}
.wrap{width:1004px;margin:0 auto;position:relative}

/* header */
.site-header{height:90px;border-top:4px solid var(--red);background:var(--white);position:relative}
.brand{position:absolute;left:98px;top:22px;font-family:"Raleway",Arial,sans-serif;font-weight:800;font-size:30px;color:var(--ink);letter-spacing:-.5px;line-height:40px}
.main-nav{position:absolute;right:98px;top:0;height:86px;display:flex;align-items:center;gap:38px}
.main-nav a{font-family:"Raleway",Arial,sans-serif;font-weight:700;font-size:14px;color:var(--ink);text-decoration:none;position:relative}
.main-nav a.is-active{color:var(--red)}
.main-nav a.is-active::after{content:"";position:absolute;left:0;right:0;bottom:-8px;height:5px;border-top:1px solid var(--red);border-bottom:1px solid var(--red)}
.nav-sep{width:1px;height:20px;background:#cccccc;margin-right:-14px}
.search-icon{width:16px;height:16px}

/* hero */
.hero{height:528px;position:relative;overflow:hidden;background:linear-gradient(135deg,#3e5a85 0%,#7a5f6a 30%,#a06a4a 50%,#345a8c 75%,#23406a 100%)}
.hero-title-block{position:absolute;left:0;right:0;top:190px;text-align:center}
.hero-title{font-family:"Raleway",Arial,sans-serif;font-weight:800;font-size:66px;color:var(--white);letter-spacing:1px;line-height:90px;display:inline-block;padding:6px 0;border-top:2px solid var(--white);border-bottom:2px solid var(--white);box-shadow:0 -8px 0 -6px var(--white),0 8px 0 -6px var(--white)}
.hero-arrow{position:absolute;top:236px;width:56px;height:56px;border-radius:50%;background:rgba(0,0,0,.35);display:flex;align-items:center;justify-content:center}
.hero-arrow.prev{left:24px}
.hero-arrow.next{right:24px}
.hero-dots{position:absolute;bottom:36px;left:0;right:0;display:flex;justify-content:center;gap:6px}
.hero-dots span{width:6px;height:6px;border-radius:50%;background:var(--white)}
.hero-dots span.on{background:var(--red)}

/* section titles */
.section-title{font-family:"Montserrat",Arial,sans-serif;font-weight:800;font-size:29px;color:var(--ink);display:flex;align-items:center;justify-content:center;gap:20px;text-transform:uppercase}
.section-title em{font-style:normal;color:var(--red)}
.section-title .bar{width:78px;height:7px;border-top:2px solid var(--red);border-bottom:2px solid var(--red)}
.lead{font-size:12.5px;line-height:22px;color:var(--muted);text-align:center;width:1004px;margin:22px auto 0}

/* welcome */
.welcome{padding-top:52px;height:460px}
.feature-grid{display:grid;grid-template-columns:repeat(4,1fr);margin-top:52px;text-align:center}
.feature-icon{height:72px;display:flex;align-items:center;justify-content:center}
.feature h3{font-family:"Raleway",Arial,sans-serif;font-weight:600;font-size:20px;color:var(--ink);margin-top:18px}
.feature p{font-size:12.5px;line-height:23px;color:var(--text);margin:14px auto 0;width:210px}

/* who we are */
.who{height:457px;background:var(--red);position:relative;overflow:hidden}
.who::before{content:"";position:absolute;left:-200px;top:0;width:600px;height:457px;background:linear-gradient(90deg,rgba(0,0,0,.06),rgba(0,0,0,0));transform:skewX(-30deg)}
.who-box{position:absolute;left:98px;top:63px;width:1004px;height:335px;display:flex}
.who-text{width:502px;background:var(--white);padding:78px 50px 0;text-align:center;position:relative}
.who-text::after{content:"";position:absolute;right:-22px;top:146px;border-left:22px solid var(--white);border-top:22px solid transparent;border-bottom:22px solid transparent;z-index:2}
.who-text .section-title{font-size:27px;gap:14px}
.who-text .section-title .bar{width:72px}
.who-text p{font-size:12.5px;line-height:24px;color:var(--text);margin-top:26px}
.who-photo{width:502px;height:335px;background:linear-gradient(180deg,#3d7cc4 0%,#8fb0cf 55%,#c8935a 80%,#5e4a2e 100%)}

/* projects */
.projects{padding-top:60px;height:608px}
.project-grid{display:grid;grid-template-columns:repeat(3,310px);justify-content:space-between;margin-top:34px}
.project-photo{height:175px}
.project-photo.p1{background:linear-gradient(180deg,#2b66b8 0%,#6d8fb8 55%,#a88a4a 100%)}
.project-photo.p2{background:linear-gradient(180deg,#9ab3c9 0%,#c58a5a 45%,#3a6fa0 100%)}
.project-photo.p3{background:linear-gradient(180deg,#6b6358 0%,#9d9282 55%,#c9b57a 100%)}
.project h3{font-family:"Raleway",Arial,sans-serif;font-weight:600;font-size:20px;color:var(--ink);margin-top:18px}
.project p{font-size:12.5px;line-height:24px;color:var(--text);margin-top:12px}
.btn-more{display:inline-block;margin-top:18px;height:38px;line-height:38px;padding:0 22px;background:var(--red);color:var(--white);font-family:"Raleway",Arial,sans-serif;font-weight:700;font-size:12.5px;text-transform:uppercase;position:relative;text-decoration:none}
.btn-more::after{content:"";position:absolute;right:-7px;top:0;width:3px;height:38px;background:var(--red)}

/* partners */
.partners{border-top:2px solid var(--rule);width:1004px;margin:0 auto;height:133px;display:flex;align-items:center;justify-content:space-around;padding:0 20px}
.partner-mark{background:var(--partner);height:30px;border-radius:3px}

/* footer */
.site-footer{background:var(--footer);height:256px;position:relative}
.footer-brand{position:absolute;left:98px;top:50px;font-family:"Raleway",Arial,sans-serif;font-weight:800;font-size:30px;color:var(--white)}
.footer-about{position:absolute;left:98px;top:118px;width:230px;font-size:12px;line-height:21px;color:var(--footer-text)}
.footer-col{position:absolute;top:44px}
.footer-col h4{font-family:"Raleway",Arial,sans-serif;font-weight:600;font-size:18px;color:var(--white);margin-bottom:16px}
.footer-col li{list-style:none;font-size:12px;line-height:23px;color:var(--footer-text)}
.footer-col.support{left:398px}
.footer-col.about{left:584px}
.footer-col.company{left:727px}
.footer-col.contact{left:906px;width:210px}
.contact-line{display:flex;gap:10px;font-size:12px;line-height:23px;color:var(--footer-text)}
.contact-line svg{flex:none;margin-top:6px}
.footer-bottom{position:absolute;left:0;right:0;bottom:-60px;height:60px;background:var(--footer-deep);border-top:1px solid #222}
.social{position:absolute;left:102px;top:15px;display:flex;gap:6px}
.social span{width:30px;height:30px;border-radius:50%;border:2px solid var(--white)}
.copyright{position:absolute;right:98px;top:0;line-height:60px;font-size:12px;color:var(--white)}
</style>
</head>
<body>

<header class="site-header">
  <div class="brand">Marlow Rigging</div>
  <nav class="main-nav">
    <a class="is-active" href="#">HOME</a>
    <a href="#">ABOUT</a>
    <a href="#">OUR SERVICES</a>
    <a href="#">OUR EQUIPMENT</a>
    <a href="#">PROJECTS</a>
    <a href="#">CONTACT US</a>
    <span class="nav-sep"></span>
    <svg class="search-icon" viewBox="0 0 16 16"><circle cx="6.5" cy="6.5" r="4.5" fill="none" stroke="#ec1f27" stroke-width="2"/><line x1="10" y1="10" x2="14" y2="14" stroke="#ec1f27" stroke-width="2.4"/></svg>
  </nav>
</header>

<section class="hero" role="img" aria-label="Stacked shipping containers with a container handler lifting a box at sunset">
  <div class="hero-title-block"><h1 class="hero-title">MARLOW RIGGING</h1></div>
  <div class="hero-arrow prev"><svg width="14" height="14" viewBox="0 0 14 14"><polyline points="9,2 4,7 9,12" fill="none" stroke="#fff" stroke-width="2"/></svg></div>
  <div class="hero-arrow next"><svg width="14" height="14" viewBox="0 0 14 14"><polyline points="5,2 10,7 5,12" fill="none" stroke="#fff" stroke-width="2"/></svg></div>
  <div class="hero-dots"><span></span><span class="on"></span><span></span></div>
</section>

<section class="welcome">
  <h2 class="section-title"><span class="bar"></span><span>Welcome to <em>Marlow Rigging</em></span><span class="bar"></span></h2>
  <p class="lead">Lorem ipsum dolor sit amet, consectetur adipiscing elit, sed do eiusmod tempor incididunt ut labore et dolore magna aliqua. Ut enim ad minim veniam,<br>quis nostrud exercitation ullamco laboris nisi ut aliquip ex ea commodo consequat. Duis aute irure dolor in reprehenderit in voluptate velit ess</p>
  <div class="wrap feature-grid">
    <div class="feature">
      <div class="feature-icon">
        <svg width="86" height="56" viewBox="0 0 86 56"><rect x="3" y="6" width="50" height="34" fill="none" stroke="#ec1f27" stroke-width="3"/><path d="M53 16h18l12 14v10H53z" fill="#111"/><rect x="60" y="20" width="10" height="8" fill="#fff"/><circle cx="18" cy="44" r="7" fill="#fff" stroke="#111" stroke-width="3"/><circle cx="68" cy="44" r="7" fill="#fff" stroke="#111" stroke-width="3"/></svg>
      </div>
      <h3>Semi Trucks</h3>
      <p>Sed ut perspiciatis unde omninats error sit voluptatem accusantidolore mque laudantium, totarem.</p>
    </div>
    <div class="feature">
      <div class="feature-icon">
        <svg width="76" height="64" viewBox="0 0 76 64"><path d="M8 28h30V10h10l6 18v18H8z" fill="#ec1f27"/><rect x="24" y="14" width="12" height="12" fill="#fff"/><line x1="60" y1="2" x2="60" y2="56" stroke="#111" stroke-width="4"/><line x1="60" y1="56" x2="74" y2="56" stroke="#111" stroke-width="4"/><circle cx="18" cy="50" r="8" fill="#fff" stroke="#111" stroke-width="4"/><circle cx="44" cy="50" r="8" fill="#fff" stroke="#111" stroke-width="4"/></svg>
      </div>
      <h3>Forklifts</h3>
      <p>Sed ut perspiciatis unde omninats error sit voluptatem accusantidolore mque laudantium, totarem.</p>
    </div>
    <div class="feature">
      <div class="feature-icon">
        <svg width="50" height="76" viewBox="0 0 50 76"><circle cx="25" cy="9" r="7" fill="none" stroke="#ec1f27" stroke-width="3"/><line x1="25" y1="16" x2="25" y2="28" stroke="#ec1f27" stroke-width="3"/><circle cx="25" cy="50" r="22" fill="none" stroke="#ec1f27" stroke-width="3"/><path d="M25 36v16a6 6 0 0 1-12 0" fill="none" stroke="#111" stroke-width="3"/></svg>
      </div>
      <h3>Equipments</h3>
      <p>Sed ut perspiciatis unde omninats error sit voluptatem accusantidolore mque laudantium, totarem.</p>
    </div>
    <div class="feature">
      <div class="feature-icon">
        <svg width="72" height="62" viewBox="0 0 72 62"><line x1="6" y1="10" x2="34" y2="4" stroke="#ec1f27" stroke-width="5"/><line x1="20" y1="8" x2="20" y2="22" stroke="#111" stroke-width="2"/><rect x="10" y="22" width="20" height="14" fill="none" stroke="#ec1f27" stroke-width="3"/><rect x="38" y="8" width="26" height="26" fill="none" stroke="#111" stroke-width="3"/><rect x="44" y="14" width="14" height="10" fill="#111"/><rect x="4" y="40" width="64" height="10" fill="none" stroke="#111" stroke-width="3"/><circle cx="14" cy="56" r="4" fill="#ec1f27"/><circle cx="36" cy="56" r="4" fill="#ec1f27"/><circle cx="58" cy="56" r="4" fill="#ec1f27"/></svg>
      </div>
      <h3>Machinery Moving</h3>
      <p>Sed ut perspiciatis unde omninats error sit voluptatem accusantidolore mque laudantium, totarem.</p>
    </div>
  </div>
</section>

<section class="who">
  <div class="who-box">
    <div class="who-text">
      <h2 class="section-title"><span class="bar"></span><span>Who <em>We Are</em></span><span class="bar"></span></h2>
      <p>Lorem ipsum dolor sit amet, consectetur adipiscing elit, sed do eiumod tinc idiunt ut labore et dolore magna aliquat enim ad minim veniam, quis nostrud exercitation ullamco laboris nisi ut aliquip ex ea commodo consequatis aute irure dolor in reprehenderit in voluptate velit ess nostrud exercitation ullamcoLorem ipsum dolor sit amet, consectetur adipiscing elit, sed do eiumod .</p>
    </div>
    <div class="who-photo" role="img" aria-label="Oil pump jack in a field under a blue evening sky"></div>
  </div>
</section>

<section class="projects">
  <h2 class="section-title"><span class="bar"></span><span>Our <em>Projects</em></span><span class="bar"></span></h2>
  <p class="lead">Lorem ipsum dolor sit amet, consectetur adipiscing elit, sed do eiusmod tempor incididunt ut labore et dolore magna aliqua. Ut enim ad minim veniam,<br>quis nostrud exercitation ullamco laboris nisi ut aliquip ex ea commodo consequat. Duis aute irure dolor in reprehenderit in voluptate velit ess</p>
  <div class="wrap project-grid">
    <article class="project">
      <div class="project-photo p1" role="img" aria-label="Yellow container handler lifting a shipping container in a port yard"></div>
      <h3>Finibs Bono Malorum</h3>
      <p>Sed ut perlospiciatis unde omloreiste natus error sit volupta lortem accusan tium doloremque laudloan tiumotam rem aperiameaque isapta.</p>
      <a class="btn-more" href="#">Read More</a>
    </article>
    <article class="project">
      <div class="project-photo p2" role="img" aria-label="Aerial view of a busy container port with cranes and a cargo ship"></div>
      <h3>Finibs Bono Malorum</h3>
      <p>Sed ut perlospiciatis unde omloreiste natus error sit volupta lortem accusan tium doloremque laudloan tiumotam rem aperiameaque isapta.</p>
      <a class="btn-more" href="#">Read More</a>
    </article>
    <article class="project">
      <div class="project-photo p3" role="img" aria-label="Forklift working between shelves in a warehouse"></div>
      <h3>Finibs Bono Malorum</h3>
      <p>Sed ut perlospiciatis unde omloreiste natus error sit volupta lortem accusan tium doloremque laudloan tiumotam rem aperiameaque isapta.</p>
      <a class="btn-more" href="#">Read More</a>
    </article>
  </div>
</section>

<section class="partners" aria-label="Partners">
  <span class="partner-mark" style="width:180px"></span>
  <span class="partner-mark" style="width:52px;height:52px;border-radius:50%"></span>
  <span class="partner-mark" style="width:104px;height:36px"></span>
  <span class="partner-mark" style="width:168px"></span>
  <span class="partner-mark" style="width:150px"></span>
</section>

<footer class="site-footer">
  <div class="footer-brand">Marlow Rigging</div>
  <p class="footer-about">Sed ut perspiciatis unde omnis istenats error sit voluptatem accusantium dolou eotam rem aperiamed ut perspiciati.</p>
  <div class="footer-col support">
    <h4>Support</h4>
    <ul><li>Heavy Lifting Services</li><li>Transport Services</li><li>Forklifts,</li><li>Similar Equipments</li><li>Semi Trucks</li></ul>
  </div>
  <div class="footer-col about">
    <h4>About</h4>
    <ul><li>Our News</li><li>Blog</li><li>Research</li><li>Recruitment</li><li>Careers</li></ul>
  </div>
  <div class="footer-col company">
    <h4>Company</h4>
    <ul><li>Home</li><li>About Us</li><li>Services</li><li>Projects</li><li>News</li><li>Contact</li></ul>
  </div>
  <div class="footer-col contact">
    <h4>Get In Touch</h4>
    <div class="contact-line"><svg width="9" height="12" viewBox="0 0 9 12"><path d="M4.5 0A4.5 4.5 0 0 0 0 4.5C0 8 4.5 12 4.5 12S9 8 9 4.5A4.5 4.5 0 0 0 4.5 0z" fill="#ec1f27"/><circle cx="4.5" cy="4.5" r="1.6" fill="#0e0e0e"/></svg><span>Tulsa Yard Office, 214<br>Harbor Line Road</span></div>
    <div class="contact-line"><svg width="10" height="10" viewBox="0 0 10 10"><path d="M2 0l2 2.5-1.2 1.3a6 6 0 0 0 3.4 3.4L7.5 6 10 8l-1.5 2C4 10 0 6 0 1.5z" fill="#ec1f27"/></svg><span>Phone:555.018.4420</span></div>
    <div class="contact-line"><svg width="11" height="8" viewBox="0 0 11 8"><rect width="11" height="8" fill="#ec1f27"/><polyline points="0,0 5.5,4.5 11,0" fill="none" stroke="#0e0e0e" stroke-width="1.2"/></svg><span>Email: info@marlowrigging.com</span></div>
  </div>
  <div class="footer-bottom">
    <div class="social"><span></span><span></span><span></span><span></span></div>
    <div class="copyright">© 2017 Marlow Rigging. All Copyrights are reserved. Privacy Policy</div>
  </div>
</footer>

</body>
</html>
```